UX/UI Design of mobile application for language learning through picture cards

We are looking for a Mobile Application Designer with knowledge of UX/UI concepts.

We best candidate is a skilled Mobile Application Designer with knowledge of last trends and with experience in completing similar tasks.

This is a test task. After successful completion, the best candidate will be given a full task.

```html
<!DOCTYPE html>
<html lang="en">
<head>
<meta charset="utf-8">
<title>WordSnap – Mobile App Screens</title>
<link href="https://fonts.googleapis.com/css2?family=PT+Serif:wght@400;700&family=Roboto:wght@400;500&display=swap" rel="stylesheet">
<style>
:root{
  --bg:#f1f3f6;
  --frame:#f7f8fb;
  --violet:#b08ae0;
  --lilac:#c9b4ee;
  --periwinkle:#8fa4e0;
  --panel:rgba(255,255,255,.28);
  --ink:#1d1b2b;
  --muted:#5d5a72;
  --blue:#1e86f4;
  --green:#4fd067;
  --chip:#ffffff;
  --alert:#f0365c;
  --icon:#3a3748;
}
*{box-sizing:border-box;margin:0;padding:0}
html,body{width:1200px;height:2291px;overflow:hidden}
body{background:var(--bg);position:relative;font-family:"Roboto",sans-serif;color:var(--ink)}
.sprites{position:absolute;width:0;height:0}
.phone{position:absolute;width:265px;height:560px;border-radius:42px;background:var(--frame);padding:14px;box-shadow:0 18px 40px rgba(90,80,130,.18)}
.phone.tilt{transform:rotate(45deg) scale(.95)}
.screen{position:relative;width:100%;height:100%;border-radius:32px;overflow:hidden;
  background:linear-gradient(160deg,var(--violet) 0%,var(--lilac) 35%,var(--periwinkle) 55%,var(--violet) 100%)}
.notch{position:absolute;left:50%;top:0;width:130px;height:20px;margin-left:-65px;background:var(--frame);border-radius:0 0 16px 16px}
.panel{position:absolute;left:16px;right:16px;top:42px;bottom:36px;border-radius:26px;background:var(--panel)}
.title{position:absolute;left:20px;top:20px;font-family:"PT Serif",serif;line-height:1}
.title small{display:block;font-size:13px}
.title b{font-size:20px}
.tag{position:absolute;right:16px;top:42px;font-size:8px;color:var(--muted)}
.plus-btn{position:absolute;right:-6px;top:-6px;width:22px;height:22px;border-radius:50%;background:var(--blue);display:flex;align-items:center;justify-content:center}
.plus-btn svg{width:10px;height:10px}
.grid{position:absolute;left:20px;top:68px;display:grid;grid-template-columns:80px 80px;gap:11px 13px}
.tile{position:relative;height:104px;border-radius:10px;overflow:hidden}
.tile span{position:absolute;left:0;right:0;bottom:6px;text-align:center;font-size:8px;color:#fff}
.tile.add{background:var(--blue)}
.tile.add svg{position:absolute;left:24px;top:30px;width:32px;height:32px}
.p1{background:linear-gradient(160deg,#c8c4b8,#8d8a82)}
.p2{background:linear-gradient(160deg,#e9e7ec,#b7343c)}
.p3{background:linear-gradient(160deg,#7d7873,#3c3a39)}
.p4{background:linear-gradient(160deg,#2d5a9c,#e1542a)}
.p5{background:linear-gradient(160deg,#7a8790,#a9c9cf)}
.photo{position:absolute;left:20px;top:70px;width:170px;height:180px;border-radius:14px;background:linear-gradient(170deg,#e6e8ec,#9aa0a9 70%,#5e4a3c)}
.marker{position:absolute;left:58px;top:72px;width:28px;height:20px;border:1.5px solid var(--alert)}
.marker em{position:absolute;left:-4px;top:19px;background:var(--alert);color:#fff;font-size:5px;font-style:normal;padding:1px 3px;white-space:nowrap}
.tools{position:absolute;left:24px;top:262px;width:166px;display:flex;justify-content:space-between}
.tool{width:22px;height:22px;border-radius:6px;background:rgba(255,255,255,.45);box-shadow:0 2px 4px rgba(80,60,120,.15);display:flex;align-items:center;justify-content:center}
.tool svg{width:14px;height:14px}
.chips{position:absolute;left:20px;top:316px;width:180px;display:flex;flex-wrap:wrap;gap:10px 8px}
.chip{background:var(--chip);border-radius:10px;font-size:8px;padding:4px 10px;white-space:nowrap}
.chip.on{background:var(--blue);color:#fff}
.sound{position:absolute;left:20px;bottom:12px;width:26px;height:26px;border-radius:50%;background:var(--blue);display:flex;align-items:center;justify-content:center}
.sound svg{width:14px;height:14px}
.next{position:absolute;right:-2px;bottom:-10px;width:46px;height:46px;border-radius:50%;background:var(--blue);box-shadow:0 6px 14px rgba(30,134,244,.35);display:flex;align-items:center;justify-content:center}
.next svg{width:20px;height:20px}
.badge{position:absolute;left:50%;top:303px;width:52px;height:52px;margin-left:-26px;border-radius:50%;background:var(--green);display:flex;align-items:center;justify-content:center;box-shadow:0 4px 10px rgba(79,208,103,.35)}
.badge svg{width:26px;height:26px}
.congrats{position:absolute;left:0;right:0;top:369px;text-align:center;font-family:"PT Serif",serif;font-weight:700;font-size:11px}
.note{position:absolute;left:24px;right:24px;top:386px;text-align:center;font-size:6px;line-height:1.3;color:var(--muted)}
.splash{position:absolute;left:0;right:0;top:262px;text-align:center}
.splash .name{font-family:"PT Serif",serif;font-size:15px;color:var(--muted)}
.splash .claim{font-size:8px;color:#fff;margin-top:6px}
.brand{position:absolute;left:806px;top:1958px;width:370px;text-align:center}
.brand .name{font-family:"PT Serif",serif;font-size:52px;color:#6f6c78;line-height:1}
.brand .claim{font-size:27px;margin-top:12px}
.brand .desc{font-size:9px;color:var(--muted);margin-top:16px;line-height:1.25}
</style>
</head>
<body>

<svg class="sprites" aria-hidden="true">
  <symbol id="i-select" viewBox="0 0 16 16"><rect x="2" y="2" width="12" height="12" rx="2" fill="none" stroke="var(--icon)" stroke-width="1.4" stroke-dasharray="2 2"/><path d="M6 10l4-4M7 6h3v3" fill="none" stroke="var(--icon)" stroke-width="1.4"/></symbol>
  <symbol id="i-palette" viewBox="0 0 16 16"><path d="M8 2a6 6 0 0 1 6 6" fill="none" stroke="#f04b6a" stroke-width="2.4"/><path d="M14 8a6 6 0 0 1-6 6" fill="none" stroke="#2bb3e8" stroke-width="2.4"/><path d="M8 14a6 6 0 0 1-6-6" fill="none" stroke="#8bd44a" stroke-width="2.4"/><path d="M2 8a6 6 0 0 1 6-6" fill="none" stroke="#f6b73c" stroke-width="2.4"/><circle cx="8" cy="8" r="2" fill="var(--icon)"/></symbol>
  <symbol id="i-text" viewBox="0 0 16 16"><path d="M4 4h8M8 4v9M6.5 13h3" fill="none" stroke="var(--icon)" stroke-width="1.5"/><path d="M1.5 3.5v-2h2M12.5 1.5h2v2M14.5 12.5v2h-2M3.5 14.5h-2v-2" fill="none" stroke="var(--icon)" stroke-width="1"/></symbol>
  <symbol id="i-crop" viewBox="0 0 16 16"><rect x="3" y="3" width="10" height="10" fill="none" stroke="var(--icon)" stroke-width="1.2"/><g fill="#fff" stroke="var(--icon)" stroke-width="1"><rect x="1.5" y="1.5" width="3" height="3"/><rect x="11.5" y="1.5" width="3" height="3"/><rect x="1.5" y="11.5" width="3" height="3"/><rect x="11.5" y="11.5" width="3" height="3"/></g></symbol>
  <symbol id="i-arrow" viewBox="0 0 20 20"><path d="M3 10h13M11 5l5 5-5 5" fill="none" stroke="#fff" stroke-width="2.4" stroke-linecap="round" stroke-linejoin="round"/></symbol>
  <symbol id="i-plus" viewBox="0 0 10 10"><path d="M5 1v8M1 5h8" stroke="#fff" stroke-width="1.8" stroke-linecap="round"/></symbol>
  <symbol id="i-sound" viewBox="0 0 16 16"><path d="M2 6h3l4-3v10l-4-3H2z" fill="none" stroke="#fff" stroke-width="1.3" stroke-linejoin="round"/><path d="M11 5.5a3.5 3.5 0 0 1 0 5M12.8 3.8a6 6 0 0 1 0 8.4" fill="none" stroke="#fff" stroke-width="1.2" stroke-linecap="round"/></symbol>
  <symbol id="i-check" viewBox="0 0 26 26"><path d="M6 13.5l5 5 9-10" fill="none" stroke="#fff" stroke-width="3.4" stroke-linecap="round" stroke-linejoin="round"/></symbol>
</svg>

<!-- tilted showcase -->
<div class="phone tilt" style="left:214px;top:-18px"><div class="screen"><div class="notch"></div>
  <div class="splash"><div class="name">WordSnap</div><div class="claim">Your Language Teacher</div></div>
</div></div>

<div class="phone tilt" style="left:672px;top:-22px"><div class="screen"><div class="notch"></div>
  <div class="panel">
    <div class="title"><small>Picture</small><b>Gellary</b></div>
    <div class="grid">
      <div class="tile p1" role="img" aria-label="Kitchen photo"><span>Kitchen</span></div>
      <div class="tile p2" role="img" aria-label="Shop photo"><span>Shop</span></div>
      <div class="tile p3" role="img" aria-label="Architecture photo"><span>Architecture</span></div>
      <div class="tile p4" role="img" aria-label="Accessories photo"><span>Accessories</span></div>
      <div class="tile p5" role="img" aria-label="Playground photo"><span>Playgound</span></div>
      <div class="tile add"><svg><use href="#i-plus"/></svg><span>Add Picture</span></div>
    </div>
  </div>
</div></div>

<div class="phone tilt" style="left:240px;top:393px"><div class="screen"><div class="notch"></div>
  <div class="panel">
    <div class="plus-btn"><svg><use href="#i-plus"/></svg></div>
    <div class="title"><small>Picture</small><b>Gellary</b></div><div class="tag">Kitchen</div>
    <div class="photo" role="img" aria-label="Kitchen interior photo"><div class="marker"><em>Microwave</em></div></div>
    <div class="tools"><div class="tool"><svg><use href="#i-select"/></svg></div><div class="tool"><svg><use href="#i-palette"/></svg></div><div class="tool"><svg><use href="#i-text"/></svg></div><div class="tool"><svg><use href="#i-crop"/></svg></div></div>
    <div class="chips"><span class="chip on">Microondas</span><span class="chip">Micreathonn</span><span class="chip">Microonde</span><span class="chip">микроталасна</span><span class="chip">mikrohullámú sütő</span><span class="chip">hawewe uila</span></div>
    <div class="sound"><svg><use href="#i-sound"/></svg></div><div class="next"><svg><use href="#i-arrow"/></svg></div>
  </div>
</div></div>

<div class="phone tilt" style="left:598px;top:495px"><div class="screen"><div class="notch"></div>
  <div class="panel">
    <div class="plus-btn"><svg><use href="#i-plus"/></svg></div>
    <div class="title"><small>Picture</small><b>Gellary</b></div><div class="tag">Kitchen</div>
    <div class="photo" role="img" aria-label="Kitchen interior photo"><div class="marker"><em>Microwave</em></div></div>
    <div class="tools"><div class="tool"><svg><use href="#i-select"/></svg></div><div class="tool"><svg><use href="#i-palette"/></svg></div><div class="tool"><svg><use href="#i-text"/></svg></div><div class="tool"><svg><use href="#i-crop"/></svg></div></div>
    <div class="badge"><svg><use href="#i-check"/></svg></div>
    <div class="congrats">Congratulations</div>
    <div class="note">The user sees the pictures one by one. In each picture, the user must correctly align all the selected objects</div>
    <div class="next"><svg><use href="#i-arrow"/></svg></div>
  </div>
</div></div>

<!-- upright composition -->
<div class="phone" style="left:52px;top:1021px"><div class="screen"><div class="notch"></div>
  <div class="splash"><div class="name">WordSnap</div><div class="claim">Your Language Teacher</div></div>
</div></div>

<div class="phone" style="left:816px;top:1069px"><div class="screen"><div class="notch"></div>
  <div class="panel">
    <div class="title"><small>Picture</small><b>Gellary</b></div>
    <div class="grid">
      <div class="tile p1" role="img" aria-label="Kitchen photo"><span>Kitchen</span></div>
      <div class="tile p2" role="img" aria-label="Shop photo"><span>Shop</span></div>
      <div class="tile p3" role="img" aria-label="Architecture photo"><span>Architecture</span></div>
      <div class="tile p4" role="img" aria-label="Accessories photo"><span>Accessories</span></div>
      <div class="tile p5" role="img" aria-label="Playground photo"><span>Playgound</span></div>
      <div class="tile add"><svg><use href="#i-plus"/></svg><span>Add Picture</span></div>
    </div>
  </div>
</div></div>

<div class="phone" style="left:473px;top:1461px"><div class="screen"><div class="notch"></div>
  <div class="panel">
    <div class="plus-btn"><svg><use href="#i-plus"/></svg></div>
    <div class="title"><small>Picture</small><b>Gellary</b></div><div class="tag">Kitchen</div>
    <div class="photo" role="img" aria-label="Kitchen interior photo"><div class="marker"><em>Microwave</em></div></div>
    <div class="tools"><div class="tool"><svg><use href="#i-select"/></svg></div><div class="tool"><svg><use href="#i-palette"/></svg></div><div class="tool"><svg><use href="#i-text"/></svg></div><div class="tool"><svg><use href="#i-crop"/></svg></div></div>
    <div class="chips"><span class="chip on">Microondas</span><span class="chip">Micreathonn</span><span class="chip">Microonde</span><span class="chip">микроталасна</span><span class="chip">mikrohullámú sütő</span><span class="chip">hawewe uila</span></div>
    <div class="sound"><svg><use href="#i-sound"/></svg></div><div class="next"><svg><use href="#i-arrow"/></svg></div>
  </div>
</div></div>

<div class="phone" style="left:122px;top:1652px"><div class="screen"><div class="notch"></div>
  <div class="panel">
    <div class="plus-btn"><svg><use href="#i-plus"/></svg></div>
    <div class="title"><small>Picture</small><b>Gellary</b></div><div class="tag">Kitchen</div>
    <div class="photo" role="img" aria-label="Kitchen interior photo"><div class="marker"><em>Microwave</em></div></div>
    <div class="tools"><div class="tool"><svg><use href="#i-select"/></svg></div><div class="tool"><svg><use href="#i-palette"/></svg></div><div class="tool"><svg><use href="#i-text"/></svg></div><div class="tool"><svg><use href="#i-crop"/></svg></div></div>
    <div class="badge"><svg><use href="#i-check"/></svg></div>
    <div class="congrats">Congratulations</div>
    <div class="note">The user sees the pictures one by one. In each picture, the user must correctly align all the selected objects</div>
    <div class="next"><svg><use href="#i-arrow"/></svg></div>
  </div>
</div></div>

<div class="brand">
  <div class="name">WordSnap</div>
  <div class="claim">Your Language Teacher</div>
  <p class="desc">Design layout in any format convenient for you with descriptions of<br>interactions with the interface<br>Logo mockup with vector graphics<br>You have the complete creative freedom to choose colors, interface design<br>elements, placement of elements, and interactions with the interface</p>
</div>

</body>
</html>
```